Invitation Design Project

50th Birthday Party for Tim. Big, loud party planned with loads of friends and family. at our home. Decorations will be coloured lanterns attached to the pergola and hired a band.

Details:

on 19th October, 2013
(other details when design chosen)
at: 7.00 pm
RSVP: 14th October, 2013

```html
<!DOCTYPE html>
<html lang="en">
<head>
<meta charset="utf-8">
<title>Tim's 50th Birthday Party Invitation</title>
<link rel="stylesheet" href="https://fonts.googleapis.com/css2?family=Arimo:wght@400;700&display=swap">
<style>
  :root {
    --ink-black: #000000;
    --text-white: #ffffff;
    --glow-magenta: #d6197c;
    --glow-red: #e8312a;
    --glow-orange: #f39a1e;
    --glow-yellow: #f5e51c;
    --glow-green: #4cbf3a;
    --glow-cyan: #1fb3d9;
    --glow-blue: #2a4fb8;
    --glow-violet: #6a2b9a;
  }
  html, body {
    margin: 0;
    padding: 0;
    background: var(--ink-black);
    overflow: hidden;
  }
  .invitation {
    position: relative;
    width: 849px;
    height: 1200px;
    background: var(--ink-black);
    overflow: hidden;
    font-family: "Arimo", Arial, sans-serif;
    color: var(--text-white);
    text-align: center;
  }
  .party-scene {
    position: absolute;
    top: 0;
    left: 0;
    width: 849px;
    height: 720px;
  }
  .headline {
    position: absolute;
    top: 14px;
    left: 0;
    width: 100%;
    margin: 0;
    font-size: 42px;
    font-weight: 700;
    letter-spacing: 0.5px;
  }
  .verse {
    position: absolute;
    left: 0;
    width: 100%;
    margin: 0;
    line-height: 38px;
  }
  .verse-lead {
    top: 706px;
    font-size: 30px;
    font-weight: 700;
  }
  .verse-invite {
    top: 818px;
    font-size: 28px;
    font-weight: 400;
  }
  .event-title {
    position: absolute;
    top: 944px;
    left: 0;
    width: 100%;
    margin: 0;
    font-size: 46px;
    font-weight: 700;
  }
  .event-date {
    position: absolute;
    top: 1004px;
    left: 0;
    width: 100%;
    margin: 0;
    font-size: 34px;
    font-weight: 700;
    word-spacing: 2px;
  }
  .event-details {
    position: absolute;
    top: 1080px;
    left: 0;
    width: 100%;
    margin: 0;
    font-size: 22px;
    line-height: 32px;
  }
</style>
</head>
<body>
<main class="invitation">
  <svg class="party-scene" viewBox="0 0 849 720" role="img" aria-label="Disco party scene: a mirrored disco ball hanging among coloured lanterns and rainbow light beams, above a crowd of dancing guests in silhouette with arms raised">
    <defs>
      <linearGradient id="rainbow-light" x1="0" y1="0" x2="1" y2="0">
        <stop offset="0" stop-color="var(--glow-magenta)"/>
        <stop offset="0.18" stop-color="var(--glow-red)"/>
        <stop offset="0.35" stop-color="var(--glow-orange)"/>
        <stop offset="0.5" stop-color="var(--glow-yellow)"/>
        <stop offset="0.65" stop-color="var(--glow-green)"/>
        <stop offset="0.8" stop-color="var(--glow-cyan)"/>
        <stop offset="0.92" stop-color="var(--glow-blue)"/>
        <stop offset="1" stop-color="var(--glow-violet)"/>
      </linearGradient>
      <linearGradient id="fade-to-night" x1="0" y1="0" x2="0" y2="1">
        <stop offset="0" stop-color="#000" stop-opacity="0.75"/>
        <stop offset="0.22" stop-color="#000" stop-opacity="0.15"/>
        <stop offset="0.5" stop-color="#000" stop-opacity="0"/>
        <stop offset="0.72" stop-color="#000" stop-opacity="0.55"/>
        <stop offset="0.85" stop-color="#000" stop-opacity="1"/>
        <stop offset="1" stop-color="#000" stop-opacity="1"/>
      </linearGradient>
    </defs>
    <rect width="849" height="720" fill="url(#rainbow-light)"/>
    <rect width="849" height="720" fill="url(#fade-to-night)"/>
  </svg>

  <h1 class="headline">Tim's 50th Birthday Party</h1>

  <p class="verse verse-lead">The big 5-0 is approaching fast<br>Tim is over the hill at last!</p>

  <p class="verse verse-invite">Come celebrate and spread some cheer<br>And let Gavin know he's old this year!</p>

  <h2 class="event-title">Tim's 50th Birthday Party</h2>
  <p class="event-date">19th October, 2013,&nbsp; 7.00 pm</p>

  <p class="event-details">Tim's Home<br>RSVP&nbsp; 14th October, 2013</p>
</main>
</body>
</html>
```